Pediatric Vision Care: Myopia Control Brochure

We are a pediatric eye care practice (ophthalmology and optometry). One of our services we offer for children is myopia control, which are strategies for slowing or stopping the progression of nearsightedness. This is a service we need to sell to parents because most insurance won't pay for it. There are different options we offer that can work well for kids in different situations: glasses with Corvane lenses, atropine eye drops, and/or special contact lenses. We need a brochure we can distribute to parents to let them know about this service that would encourage them to buy it for children who need it. Attached is our initial draft brochure created by our staff that provides text that we want to keep. The images and layout can change. We probably need at least one or two photos of kids on the brochure, because this is only something that works for children who are still growing, and the target audience is parents of 4-8 year old children.

Target Market(s)

Parents of 4-8 year old children

Font styles to use
Sans Serif

Requirements
Must have
• I'm uploading our company logo that should be included somewhere on the brochure. You can include contact information (web address, phone number) for our practice that is found on our website: http://www.brookhollowkidsvision.com/
Should not have
• This should not look childish. We need the impression to be friendly but professional, medical, expert.

```html
<!DOCTYPE html>
<html lang="en">
<head>
<meta charset="utf-8">
<title>Myopia Control Brochure</title>
<link href="https://fonts.googleapis.com/css2?family=Montserrat:wght@200;400;500;700;800&display=swap" rel="stylesheet">
<style>
  :root {
    --backdrop: #c4c4c4;
    --paper: #f2f3f3;
    --navy: #1c2947;
    --blue: #1f5aa6;
    --blue-deep: #174a8c;
    --green: #8cc63f;
    --green-soft: #9ccb4e;
    --teal: #0f3a52;
    --ink: #2b2f36;
    --white: #ffffff;
  }
  * { box-sizing: border-box; margin: 0; padding: 0; }
  html, body { width: 1200px; height: 800px; overflow: hidden; }
  body {
    background: var(--backdrop);
    font-family: "Montserrat", sans-serif;
    color: var(--ink);
    display: flex;
    align-items: center;
    justify-content: center;
    gap: 20px;
  }
  .spread {
    display: flex;
    width: 570px;
    height: 440px;
    box-shadow: 0 10px 24px rgba(0,0,0,.18);
  }
  .panel {
    position: relative;
    width: 190px;
    height: 440px;
    background: var(--paper);
    overflow: hidden;
  }
  .panel + .panel { border-left: 1px solid rgba(0,0,0,.06); }
  .layer { position: absolute; inset: 0; width: 100%; height: 100%; }
  .photo { position: absolute; }
  .body-copy {
    position: absolute;
    left: 18px; right: 18px;
    font-size: 6px;
    line-height: 1.5;
    text-align: center;
  }
  .body-copy p + p { margin-top: 7px; }
  .panel-heading {
    position: absolute;
    left: 10px; right: 10px;
    text-align: center;
    font-weight: 800;
    font-size: 12px;
    line-height: 1.05;
    color: var(--navy);
    text-transform: uppercase;
  }
  .on-blue { color: var(--white); }

  .brand-name {
    position: absolute; top: 20px; left: 0; right: 0;
    text-align: center; font-size: 9px; font-weight: 500; color: var(--navy);
  }
  .brand-name .dot {
    display: inline-block; width: 6px; height: 6px; border-radius: 50%;
    background: var(--green); margin-right: 4px; vertical-align: middle;
  }
  .cover-title {
    position: absolute; top: 40px; left: 0; right: 0; text-align: center;
    color: var(--navy); text-transform: uppercase; line-height: 1;
  }
  .cover-title .strong { display: block; font-weight: 800; font-size: 23px; }
  .cover-title .light { display: block; font-weight: 200; font-size: 23px; }

  .contact-list {
    position: absolute; top: 282px; left: 10px; right: 10px;
    text-align: center; color: var(--white); font-size: 6.2px; line-height: 1.45;
  }
  .contact-item + .contact-item { margin-top: 9px; }
  .contact-item svg { width: 9px; height: 9px; display: block; margin: 0 auto 2px; }
  .contact-label { font-weight: 700; }
</style>
</head>
<body>

<section class="spread spread-outside">
  <article class="panel panel-environment">
    <div class="body-copy" style="top:40px">
      <p>All myopic children can benefit from these lifestyle changes. It is important to get your child outdoors consistently. There is strong evidence that children who spend at least 2 hours a day outdoors are less likely to become myopic, and their myopia progresses slower than children who are outdoors less. Some studies show that increasing outdoor time by as few as 45 minutes a day is beneficial in reducing progression.</p>
      <p>There is some evidence that consistent use of screens, particularly held very close to the face, can worsen nearsightedness. We recommend limiting nonacademic screen time and near work, and encourage your child to use the 20-20-20 rule. Every 20 minutes take a 20 second break to look at least 20 feet away.</p>
    </div>
    <h2 class="panel-heading" style="top:232px">Environmental<br>Options:</h2>
    <svg class="layer" viewBox="0 0 190 440" aria-hidden="true">
      <path d="M120 300 Q160 280 190 250 L190 440 L120 440 Z" fill="var(--green)"/>
      <path d="M130 310 Q165 292 190 268 L190 440 L130 440 Z" fill="var(--blue)"/>
      <path d="M0 400 Q40 430 90 440 L0 440 Z" fill="var(--green)"/>
      <circle cx="88" cy="368" r="70" fill="var(--blue)"/>
      <circle cx="88" cy="368" r="56" fill="var(--green)"/>
      <circle cx="88" cy="368" r="51" fill="var(--paper)"/>
    </svg>
    <div class="photo" role="img" aria-label="Close-up photo of a child's eye with a digital scan overlay"
         style="left:39px;top:319px;width:98px;height:98px;border-radius:50%;background:linear-gradient(160deg,#c9dbe6 0%,#dcd6d2 55%,#cdbdb3 100%)"></div>
  </article>

  <article class="panel panel-contact" style="background:var(--green-soft)">
    <svg class="layer" viewBox="0 0 190 440" aria-hidden="true">
      <circle cx="38" cy="58" r="24" fill="var(--blue)"/>
      <circle cx="18" cy="28" r="4" fill="var(--blue)"/>
      <rect x="0" y="262" width="190" height="178" fill="var(--blue)"/>
    </svg>
    <div class="photo" role="img" aria-label="Eye doctor fitting a trial frame on a young child"
         style="left:40px;top:8px;width:145px;height:185px;background:linear-gradient(170deg,#e8ebef 0%,#cfd6df 45%,#b9c58e 100%)"></div>
    <h2 class="panel-heading on-blue" style="top:208px;font-size:11px">Contact<br>and Scheduling<br>Info</h2>
    <div class="contact-list">
      <div class="contact-item">
        <svg viewBox="0 0 10 10" aria-hidden="true"><circle cx="5" cy="5" r="5" fill="#fff"/><path d="M3.3 2.8l1 .9-.5.8c.4.7.9 1.2 1.5 1.5l.8-.5.9 1-.6.8C4.8 7.2 2.9 5.4 2.6 3.5z" fill="var(--blue)"/></svg>
        <div class="contact-label">NUMBER:</div>
        <div>Voice: (555) 210-4400</div>
        <div>Text: (555) 210-4411</div>
        <div>Fax: (555) 210-4422</div>
      </div>
      <div class="contact-item">
        <svg viewBox="0 0 10 10" aria-hidden="true"><circle cx="5" cy="5" r="5" fill="#fff"/><rect x="2.6" y="3.3" width="4.8" height="3.4" fill="var(--blue)"/><path d="M2.6 3.3L5 5.2 7.4 3.3" stroke="#fff" stroke-width=".5" fill="none"/></svg>
        <div class="contact-label">EMAIL:</div>
        <div>appointments@brookhollowkidsvision.com</div>
      </div>
      <div class="contact-item">
        <svg viewBox="0 0 10 10" aria-hidden="true"><circle cx="5" cy="5" r="5" fill="#fff"/><path d="M5 2.3a1.8 1.8 0 0 1 1.8 1.8C6.8 5.4 5 7.7 5 7.7S3.2 5.4 3.2 4.1A1.8 1.8 0 0 1 5 2.3z" fill="var(--blue)"/><circle cx="5" cy="4.1" r=".6" fill="#fff"/></svg>
        <div class="contact-label">ADDRESS:</div>
        <div>Brookhollow Kids Vision</div>
        <div>1280 Larkspur Avenue</div>
        <div>Fairhaven, VA 23000</div>
      </div>
    </div>
  </article>

  <article class="panel panel-cover">
    <div class="brand-name"><span class="dot"></span>Brookhollow Kids Vision</div>
    <h1 class="cover-title"><span class="strong">Myopia</span><span class="light">Control</span></h1>
    <div class="body-copy" style="top:100px">
      <p>Myopia or nearsightedness causes blurry distance vision. Myopia is caused by the elongation of the eye, and progresses throughout childhood. Myopia is becoming increasingly common. More severe myopia and a higher glasses prescription is associated with a higher risk of eye problems involving the retina in adulthood, such as retinal problems and macular degeneration.</p>
      <p>Myopia control is meant to slow the growth of the eye, keeping the glasses prescription as low as possible and reducing the risk of ocular disease in adulthood. There are several treatment options</p>
    </div>
    <div class="photo" role="img" aria-label="Smiling girl wearing round glasses"
         style="left:0;top:262px;width:190px;height:178px;background:linear-gradient(160deg,#eef0f2 0%,#d9dee5 50%,#9fb6d4 100%)"></div>
    <svg class="layer" viewBox="0 0 190 440" aria-hidden="true">
      <path d="M0 248 Q95 240 190 330 L190 352 Q110 268 0 270 Z" fill="var(--green)"/>
      <path d="M190 350 L190 440 L120 440 Q160 410 190 350 Z" fill="var(--blue)"/>
      <path d="M120 440 Q160 410 190 350 L190 362 Q165 418 140 440 Z" fill="var(--green)"/>
    </svg>
  </article>
</section>

<section class="spread spread-inside">
  <article class="panel panel-lenses">
    <div class="photo" role="img" aria-label="Stacked clear lenses on a light background"
         style="left:0;top:0;width:190px;height:150px;background:linear-gradient(160deg,#aebfd4 0%,#dfe6ee 60%,#f4f6f8 100%)"></div>
    <svg class="layer" viewBox="0 0 190 440" aria-hidden="true">
      <path d="M0 118 Q95 178 190 100 L190 160 L0 160 Z" fill="var(--green)"/>
      <path d="M0 132 Q95 190 190 116 L190 175 L0 175 Z" fill="var(--paper)"/>
    </svg>
    <div class="body-copy" style="top:190px">
      <p>FDA market authorized Veralux Corvane glasses lenses have been shown to slow myopia progression by about 50% in children aged 6-12.</p>
      <p>These lenses are a great treatment option because all your child needs to do is wear glasses. They look almost identical to ordinary glasses, but use specialized optics to signal the brain to slow the growth of myopic eyes.</p>
    </div>
    <h2 class="panel-heading" style="top:330px">Veralux<br>Corvane Glasses<br>Lenses</h2>
  </article>

  <article class="panel panel-atropine" style="background:var(--blue)">
    <h2 class="panel-heading on-blue" style="top:22px">Low-Dose<br>Atropine</h2>
    <div class="body-copy on-blue" style="top:60px">
      <p>These eyedrops have been studied for over 20 years and have been shown to slow myopia progression by about 50% when used consistently.</p>
      <p>Low-dose atropine is simple to add to your daily routine. One drop is placed in each eye before bed each evening. These are ordered from a compounding pharmacy and mailed directly to your home.</p>
    </div>
    <div class="photo" role="img" aria-label="Eye dropper releasing a single clear drop"
         style="left:0;top:220px;width:190px;height:220px;background:radial-gradient(ellipse at 55% 50%,#f1f1f1 0%,#d4d6d8 55%,#b9bcbf 100%)"></div>
    <svg class="layer" viewBox="0 0 190 440" aria-hidden="true">
      <path d="M0 260 Q70 175 190 235 L190 215 L0 215 Z" fill="var(--blue)"/>
      <path d="M0 262 Q70 178 190 237 L190 250 Q70 195 0 280 Z" fill="var(--green)"/>
    </svg>
  </article>

  <article class="panel panel-contacts">
    <div class="photo" role="img" aria-label="Soft contact lens resting on a fingertip"
         style="left:0;top:0;width:190px;height:170px;background:linear-gradient(150deg,var(--teal) 0%,#16495f 55%,#d9b9a4 100%)"></div>
    <svg class="layer" viewBox="0 0 190 440" aria-hidden="true">
      <path d="M0 135 Q90 205 190 120 L190 185 L0 185 Z" fill="var(--green)"/>
      <path d="M0 150 Q90 215 190 138 L190 195 L0 195 Z" fill="var(--paper)"/>
    </svg>
    <div class="body-copy" style="top:210px">
      <p>FDA-approved ClearStep lenses have been shown to slow myopia progression by about 50% in children aged 8-12.</p>
      <p>Contact lenses can be a great fit for many children, especially active children or those who do not enjoy wearing glasses. Many children as young as 7 or 8 are successful at wearing contacts.</p>
    </div>
    <h2 class="panel-heading" style="top:330px">Specialty<br>Contact Lenses</h2>
  </article>
</section>

</body>
</html>
```